Business Card Design Project

Dorran
Sales Manager

38700 Pellham Ave, Suite 415
Irvine, CA 92604

Tel: 626-555-0147
Fax: 888-555-0162
E-mail: dorran@plovetrix.com

Target Market(s)

We are the distributor and wholesaler, the business card design want to show we are a strong company.

Industry/Entity Type

Business

Colors

Designer to choose colors to be used in the design.

```html
<!DOCTYPE html>
<html lang="en">
<head>
<meta charset="utf-8">
<title>Dorran – Business Card</title>
<link href="https://fonts.googleapis.com/css2?family=Arimo:wght@400;700&family=Open+Sans:wght@600;700&display=swap" rel="stylesheet">
<style>
  :root{
    --sheet:#e4e4e4;
    --ink-dark:#08080d;
    --night:#3a3c60;
    --crimson:#7e0a24;
    --magenta:#c4077a;
    --hot-pink:#ee10b0;
    --white:#ffffff;
    --mist:#d9d9de;
  }
  *{margin:0;padding:0;box-sizing:border-box}
  html,body{width:949px;height:1200px;overflow:hidden}
  body{background:var(--sheet);position:relative;font-family:"Arimo",Arial,sans-serif}
  .card{position:absolute;left:165px;width:620px;height:399px;overflow:hidden;box-shadow:0 1px 2px rgba(0,0,0,.25)}
  .card--front{top:153px}
  .card--back{top:648px}
  .card svg.art{position:absolute;inset:0}
  .name-badge{position:absolute;left:52px;top:139px;width:186px;border-radius:6px;overflow:hidden;text-align:center}
  .name-badge__name{background:var(--ink-dark);color:var(--white);font-family:"Open Sans",Arial,sans-serif;font-weight:700;font-size:37px;line-height:50px;white-space:nowrap}
  .name-badge__title{background:linear-gradient(90deg,var(--crimson),#a50c3c);color:var(--white);font-family:"Open Sans",Arial,sans-serif;font-weight:600;font-size:22px;line-height:31px;white-space:nowrap}
  .brand-name{position:absolute;font-family:"Arimo",Arial,sans-serif;font-weight:700;text-align:center}
  .brand-name--front{left:273px;width:298px;top:86px;font-size:34px;color:var(--magenta)}
  .brand-name--back{left:0;width:620px;top:160px;font-size:42px;color:var(--mist)}
  .contact{position:absolute;left:290px;top:241px;list-style:none}
  .contact li{display:flex;align-items:center;height:34px;color:var(--white);font-size:19px;white-space:nowrap}
  .contact svg{width:36px;height:22px;margin-right:7px;flex:none}
  .address-band{position:absolute;left:0;top:325px;width:620px;height:40px;background:linear-gradient(90deg,var(--crimson),var(--magenta) 30%,var(--hot-pink) 50%,var(--magenta) 70%,var(--crimson));color:var(--white);font-size:19px;line-height:40px;text-align:center}
</style>
</head>
<body>

<section class="card card--front">
  <svg class="art" width="620" height="399" viewBox="0 0 620 399">
    <defs>
      <linearGradient id="topBerry" x1="0" x2="1" y1="0" y2="0">
        <stop offset="0" stop-color="#860a2a"/>
        <stop offset=".45" stop-color="#c80a78"/>
        <stop offset="1" stop-color="#7a0a1c"/>
      </linearGradient>
      <radialGradient id="nightGlow" cx="290" cy="370" r="330" gradientUnits="userSpaceOnUse">
        <stop offset="0" stop-color="#40426a"/>
        <stop offset=".5" stop-color="#15151f"/>
        <stop offset="1" stop-color="#06060a"/>
      </radialGradient>
      <linearGradient id="panelPink" x1="0" x2="1" y1="0" y2="1">
        <stop offset="0" stop-color="#c5087c"/>
        <stop offset=".5" stop-color="#f012b4"/>
        <stop offset="1" stop-color="#d00a8e"/>
      </linearGradient>
    </defs>
    <rect width="620" height="399" fill="url(#topBerry)"/>
    <path d="M0 173 C150 155 320 196 620 186 L620 399 L0 399 Z" fill="url(#nightGlow)"/>
    <rect x="273" y="0" width="298" height="8" fill="#1a1a28"/>
    <path d="M273 8 H571 V354 Q571 366 559 366 H285 Q273 366 273 354 Z" fill="var(--white)"/>
    <path d="M273 196 C380 214 490 212 571 200 V354 Q571 366 559 366 H285 Q273 366 273 354 Z" fill="url(#panelPink)"/>
  </svg>

  <div class="brand-name brand-name--front">Plovetrix</div>

  <div class="name-badge">
    <div class="name-badge__name">DORRAN</div>
    <div class="name-badge__title">Sales Manager</div>
  </div>

  <ul class="contact">
    <li>
      <svg viewBox="0 0 36 22" aria-hidden="true"><rect x="1" y="1" width="26" height="20" rx="3" fill="#fff"/><path d="M27 7 L34 11 L27 15 Z" fill="#fff"/><circle cx="14" cy="11" r="7" fill="none" stroke="#222" stroke-width="1.5"/><path d="M11 7 q-2 4 2 8 q2 1 3 0" fill="none" stroke="#222" stroke-width="2"/></svg>
      626-555-0147
    </li>
    <li>
      <svg viewBox="0 0 36 22" aria-hidden="true"><rect x="1" y="1" width="26" height="20" rx="3" fill="#fff"/><path d="M27 7 L34 11 L27 15 Z" fill="#fff"/><rect x="5" y="5" width="18" height="12" fill="#c00a4a"/><path d="M5 5 L14 12 L23 5 M5 17 L12 11 M23 17 L16 11" fill="none" stroke="#fff" stroke-width="1.2"/></svg>
      dorran@plovetrix.com
    </li>
    <li>
      <svg viewBox="0 0 36 22" aria-hidden="true"><rect x="1" y="1" width="26" height="20" rx="3" fill="#fff"/><path d="M27 7 L34 11 L27 15 Z" fill="#fff"/><rect x="5" y="9" width="18" height="9" fill="#222"/><rect x="9" y="4" width="10" height="6" fill="#222"/><rect x="11" y="12" width="8" height="3" fill="#fff"/></svg>
      888-555-0162
    </li>
  </ul>
</section>

<section class="card card--back">
  <svg class="art" width="620" height="399" viewBox="0 0 620 399">
    <defs>
      <radialGradient id="backGlow" cx="300" cy="185" r="330" gradientUnits="userSpaceOnUse">
        <stop offset="0" stop-color="#4a4c78"/>
        <stop offset=".45" stop-color="#1a1a28"/>
        <stop offset="1" stop-color="#050508"/>
      </radialGradient>
    </defs>
    <rect width="620" height="399" fill="url(#backGlow)"/>
  </svg>

  <div class="brand-name brand-name--back">Plovetrix</div>

  <div class="address-band">38700 Pellham Ave, Suite 415, Irvine, CA 92604</div>
</section>

</body>
</html>
```